Flash Website Intro
Animated flash intro for existing website with skip to site button
Hi Mira,
I sent you a private message regarding the updated link of my entry. Thanks
Tobin
Thank you for all your great work
I will now go through them with my partner and will let you know the decision
thanks
@Project Holder
Please check your private message and view my animation please.
http://vexloop.example/serve/5517302
Thanks
RunaFeld
dear sir,
i send link in private message. in that some clarity missing but real one is crystal clear
Hi PH, I sent you 2 link for #9
I sent you the link via private message.
for my entry#7
Hi,
Have you seen the animated version of my entry #5? I sent you the link via private message.
It is against the t&c's to send email address.
If you can upload to the internet and send me a link to view animation.
I won't be able to pick a design just from a static screenshot so please send me a link to view the full animation
thanks,
it's possible to see the animated result but we need to have ur personnal e-mail cauz here we cannot upload file larger than 2 mb . that's why
I have another doubt, banner or intro web, because I do not close their sizes
.gif format work here.
Hi
I have asked support how I view the animation rather than just a screenshot. Haven't had a response yet.
If anyone knows how I can view the flash files before I choose one please let me know
Hey i few questions:
How can uploads the swf´s
Or you want to take a screencapture of the intro.
Thank u
Please ignore the "Ad Sizes Required:" in the brief as it is just one flash banner size 880 x 325 (same as the white box on the home page of the website)

```html
<!DOCTYPE html>
<html lang="en">
<head>
<meta charset="utf-8">
<title>Creative — Intro</title>
<link rel="stylesheet" href="https://fonts.googleapis.com/css2?family=Archivo:wght@800&family=Inter:wght@400&display=swap">
<style>
  :root {
    --stage-green: #b9db9e;
    --band-green: rgba(168, 205, 140, 0.82);
    --band-edge: rgba(140, 180, 115, 0.55);
    --headline-blue: #4a9bd2;
    --skip-ink: #4f6a45;
    --arc-light: rgba(255, 255, 255, 0.35);
  }
  html, body {
    margin: 0;
    padding: 0;
    overflow: hidden;
    background: var(--stage-green);
  }
  .intro {
    position: relative;
    width: 1200px;
    height: 444px;
    overflow: hidden;
    background: var(--stage-green);
  }
  .intro__photo {
    position: absolute;
    left: 0;
    top: 0;
    width: 552px;
    height: 444px;
    background:
      radial-gradient(ellipse 260px 230px at 230px 210px, #3f9e7c 0%, #2f7f63 45%, rgba(60,90,75,0.6) 70%, rgba(0,0,0,0) 85%),
      linear-gradient(90deg, #4a4a4a 0%, #8a8a8a 35%, #b5b5b5 70%, #9fa59b 100%);
  }
  .intro__band {
    position: absolute;
    left: 396px;
    top: 0;
    width: 156px;
    height: 444px;
    background: var(--band-green);
    border-right: 1px solid var(--band-edge);
  }
  .intro__veil {
    position: absolute;
    left: 552px;
    top: 0;
    width: 648px;
    height: 444px;
    background: var(--stage-green);
  }
  .intro__arcs {
    position: absolute;
    inset: 0;
    pointer-events: none;
  }
  .intro__headline {
    position: absolute;
    left: 0;
    right: 0;
    top: 172px;
    margin: 0;
    text-align: center;
    font-family: "Archivo", "Helvetica Neue", Arial, sans-serif;
    font-weight: 800;
    font-size: 94px;
    line-height: 1;
    letter-spacing: -3px;
    color: var(--headline-blue);
  }
  .intro__skip {
    position: absolute;
    left: 0;
    right: 0;
    top: 418px;
    text-align: center;
    font-family: "Inter", Arial, sans-serif;
    font-size: 11px;
    letter-spacing: 0.2px;
    color: var(--skip-ink);
    text-decoration: none;
  }
</style>
</head>
<body>
  <main class="intro">
    <div class="intro__photo" role="img" aria-label="Close-up of a human eye in greyscale with a green iris"></div>
    <div class="intro__band"></div>
    <div class="intro__veil"></div>
    <svg class="intro__arcs" width="1200" height="444" viewBox="0 0 1200 444" aria-hidden="true">
      <path d="M 100 -10 Q 70 222 100 454" fill="none" stroke="var(--arc-light)" stroke-width="3"/>
      <path d="M 1085 -10 Q 1120 222 1085 454" fill="none" stroke="var(--arc-light)" stroke-width="3"/>
    </svg>
    <h1 class="intro__headline">CREATIVE</h1>
    <a class="intro__skip" href="#site">SKIP TO SITE</a>
  </main>
</body>
</html>
```